Business Card Design needed for start up company Pramora

In need of a new business card designed for a start up company based in Sydney, Pramora is a new start up innovative Company, our mission it to make property accessible for everyday Australian and to become the leading Real Estate platform in Australia. We want it to be fresh and clean.

Industry/Entity Type

Financial

Contact Information for Business Card

Section for Name
Section for Title

PRAMORA - Where Doors Open Wide
Mobile:
Direct:

Font styles to use
Sans Serif

Colors
33a6d7
0692cd
0255a3
ffffff

Requirements
Must have
• Logo, all business card details

```html
<!DOCTYPE html>
<html lang="en">
<head>
<meta charset="UTF-8">
<title>Pramora Business Card</title>
<link rel="stylesheet" href="https://fonts.googleapis.com/css2?family=Nunito+Sans:wght@400;700;800&display=swap">
<style>
  :root {
    --backdrop: #2a2a2b;
    --paper: #f3f3f3;
    --navy: #1f4178;
    --sky: #2a9fd8;
    --sky-light: #33a6d7;
    --ink: #4f5358;
    --rule: #c9c9c9;
    --white: #ffffff;
  }
  * { box-sizing: border-box; margin: 0; padding: 0; }
  html, body {
    width: 1200px; height: 960px; overflow: hidden;
    background: var(--backdrop);
    font-family: "Nunito Sans", Arial, sans-serif;
  }
  .card {
    position: absolute;
    width: 600px; height: 342px;
    border-radius: 20px;
    overflow: hidden;
  }
  .card-front { left: 302px; top: 124px; background: var(--paper); }
  .card-back { left: 299px; top: 493px; background: var(--navy); }

  .brand { display: flex; align-items: center; justify-content: center; position: absolute; }
  .brand-name { font-weight: 800; letter-spacing: 0.5px; line-height: 1; }

  .front-brand { left: 40px; width: 290px; top: 130px; height: 66px; }
  .front-brand .brand-name { font-size: 42px; color: var(--navy); }

  .divider {
    position: absolute; left: 327px; top: 74px;
    width: 2px; height: 180px;
    background: linear-gradient(to bottom, rgba(201,201,201,0), var(--rule) 20%, var(--rule) 80%, rgba(201,201,201,0));
  }

  .details { position: absolute; left: 356px; top: 74px; color: var(--ink); }
  .person-name { font-size: 22px; font-weight: 800; color: var(--navy); line-height: 26px; }
  .person-title { font-size: 15px; color: var(--sky); line-height: 20px; letter-spacing: 0.3px; }
  .address { margin-top: 8px; font-size: 14px; line-height: 18px; }
  .contact-list { list-style: none; margin-top: 8px; font-size: 14px; }
  .contact-list li { display: flex; align-items: center; gap: 8px; height: 19.5px; }
  .contact-list svg { width: 13px; height: 13px; fill: var(--navy); flex: none; }

  .bottom-band { position: absolute; left: 0; bottom: 0; width: 600px; height: 28px; }
  .tagline {
    position: absolute; right: 17px; bottom: 6px;
    font-size: 14px; font-weight: 700; color: var(--white); letter-spacing: 0.1px;
  }

  .back-brand { left: 0; right: 0; top: 120px; height: 104px; }
  .back-brand .brand-name { font-size: 64px; color: var(--white); }
</style>
</head>
<body>
  <section class="card card-front">
    <div class="brand front-brand">
      <span class="brand-name">PRAMORA</span>
    </div>
    <div class="divider"></div>
    <div class="details">
      <h1 class="person-name">DANIEL HAYES</h1>
      <p class="person-title">CEO/FOUNDER</p>
      <p class="address">42 Harbour Row<br>Sydney NSW 2000</p>
      <ul class="contact-list">
        <li><svg viewBox="0 0 24 24"><path d="M6.6 10.8a15.1 15.1 0 0 0 6.6 6.6l2.2-2.2c.3-.3.7-.4 1-.2 1.1.4 2.3.6 3.6.6.6 0 1 .4 1 1V20c0 .6-.4 1-1 1A17 17 0 0 1 3 4c0-.6.4-1 1-1h3.5c.6 0 1 .4 1 1 0 1.3.2 2.5.6 3.6.1.3 0 .7-.2 1z"/></svg>02 9481 6230</li>
        <li><svg viewBox="0 0 24 24"><path d="M7 1h10a2 2 0 0 1 2 2v18a2 2 0 0 1-2 2H7a2 2 0 0 1-2-2V3a2 2 0 0 1 2-2zm0 3v14h10V4zm5 15.5a1.2 1.2 0 1 0 0 2.4 1.2 1.2 0 0 0 0-2.4z"/></svg>0412 587 903</li>
        <li><svg viewBox="0 0 24 24"><path d="M2 6h20v12H2zm1.5 1.5v.4L12 13l8.5-5.1v-.4z"/></svg>daniel@pramora.com.au</li>
        <li><svg viewBox="0 0 24 24"><path d="M12 2a10 10 0 1 0 0 20 10 10 0 0 0 0-20zm-1 17.9A8 8 0 0 1 4.2 10l4.8 4.8v1a2 2 0 0 0 2 2zm6.9-2.5A2 2 0 0 0 16 16h-1v-3a1 1 0 0 0-1-1H8v-2h2a1 1 0 0 0 1-1V7h2a2 2 0 0 0 2-2v-.4a8 8 0 0 1 2.9 12.8z"/></svg>www.pramora.com.au</li>
      </ul>
    </div>
    <svg class="bottom-band" viewBox="0 0 600 28" preserveAspectRatio="none" aria-hidden="true">
      <rect x="0" y="16" width="600" height="12" fill="var(--navy)"/>
      <path d="M0 6 H390 Q395 6 397 9 L399 12 H0 Z" fill="var(--sky-light)"/>
      <path d="M384 28 V16 Q396 16 400 8 Q404 2 414 2 H600 V28 Z" fill="var(--navy)"/>
    </svg>
    <p class="tagline">Where Doors Open Wide</p>
  </section>

  <section class="card card-back">
    <div class="brand back-brand">
      <span class="brand-name">PRAMORA</span>
    </div>
  </section>
</body>
</html>
```